Book cover design about quality management systems

Book cover design that I can display in my website for ore orders
The book is about helping organisations to fully integrate their Quality management systems rather than having a quality system which sits off to the side and adds extra work.
It is aimed at organisations leaders
It is about leaders taking ownership and leading the decision and design of the quality management system and therefore being able to delegate more effectively.

Target Market(s)

CEO of government funded organisations

Industry/Entity Type

Management

Font styles to use
Sans Serif

Colors

Designer to choose colors to be used in the design.

Requirements
Must have
• Ability to be used on website
• Title of the book
• Shape steer sustain
• Strap line - Letting Quality Lead the Way
Nice to have
• Not too fussy
• Not a black cover
• Deep Yellow in the design if possible
Should not have
• Anything too feminine

```html
<!DOCTYPE html>
<html lang="en">
<head>
<meta charset="utf-8">
<title>Letting Quality Lead the Way — Book Cover</title>
<link href="https://fonts.googleapis.com/css2?family=Merriweather:wght@900&family=Oswald:wght@600&display=swap" rel="stylesheet">
<style>
  :root {
    --stage: #ffffff;
    --green-light: #7dcd6a;
    --green-mid: #5fa94c;
    --green-dark: #4f8f3f;
    --green-edge: #6cc35a;
    --piece-blue: #3aa9e6;
    --piece-yellow: #f2d22e;
    --piece-green: #6cc85a;
    --grey-light: #f6f6f6;
    --grey-mid: #d4d4d4;
    --white: #ffffff;
  }
  * { margin: 0; padding: 0; box-sizing: border-box; }
  html, body {
    width: 960px; height: 1200px; overflow: hidden;
    background: var(--stage);
  }
  .canvas { position: relative; width: 960px; height: 1200px; }
  .cover {
    position: absolute; left: 160px; top: 50px;
    width: 640px; height: 1100px;
    background: var(--green-light);
    border-top: 6px solid var(--green-edge);
    overflow: hidden;
  }
  .cover-artwork {
    position: absolute; left: 0; top: 0; width: 640px; height: 763px;
    background: radial-gradient(ellipse at 60% 40%, var(--grey-light) 0%, #e6e6e6 55%, var(--grey-mid) 100%);
  }
  .pillar {
    position: absolute; width: 190px; height: 92px;
    display: flex; align-items: center; justify-content: center;
    font-family: "Oswald", sans-serif; font-weight: 600;
    color: var(--white); font-size: 36px; letter-spacing: 1px;
    text-transform: uppercase;
    text-shadow: 1px 2px 2px rgba(0,0,0,0.35);
  }
  .pillar--shape   { left: -4px;  top: 404px; background: var(--piece-blue);   transform: rotate(-28deg); }
  .pillar--steer   { left: 158px; top: 442px; background: var(--piece-yellow); transform: rotate(-36deg); }
  .pillar--sustain { left: 423px; top: 276px; background: var(--piece-green);  transform: rotate(24deg); }
  .title-band {
    position: absolute; left: 0; top: 806px; width: 640px; height: 112px;
    border-top: 4px solid var(--white);
    border-bottom: 4px solid var(--white);
    background: var(--green-dark);
    display: flex; align-items: center; justify-content: center;
  }
  .book-title {
    font-family: "Merriweather", serif; font-weight: 900;
    font-size: 36px; color: var(--white); white-space: nowrap;
    text-shadow: 2px 2px 3px rgba(0,0,0,0.45);
  }
  .author {
    position: absolute; left: 0; right: 0; top: 1022px;
    text-align: center;
    font-family: "Merriweather", serif; font-weight: 900;
    font-size: 34px; line-height: 44px; color: var(--white); letter-spacing: 1px;
    text-shadow: 2px 2px 3px rgba(0,0,0,0.45);
  }
</style>
</head>
<body>
  <main class="canvas">
    <section class="cover">
      <div class="cover-artwork" role="img" aria-label="White jigsaw puzzle with three coloured pieces fitting into place">
        <div class="pillar pillar--shape">Shape</div>
        <div class="pillar pillar--steer">Steer</div>
        <div class="pillar pillar--sustain">Sustain</div>
      </div>
      <div class="title-band">
        <h1 class="book-title">Letting Quality Lead the Way</h1>
      </div>
      <p class="author">HELENA MARSH</p>
    </section>
  </main>
</body>
</html>
```